Oil and gas industry project solutions company needs professional cards with Canadian aboriginal fee

We are a aboriginally owned company that is focused on Project Planning, Management, Inspection & Consulting for Canada's Petroleum Industry. We have a logo that we would like to incorporate into a professional looking business card. We are professionals that offer services from project inception to completion.

Target Market(s)

Major industry leaders like NorthRidge Pipelines, Vantor, Kelstrand Energy, Brimwell etc.

Industry/Entity Type

Industry

Contact Information for Business Card

Reid Forbin
reid@kolbymarsh.ca
555 418 9067

Requirements
Must have
• KolbyMarsh Inc. logo.
• Address is: RR4, Site2, Comp7 Harlow Creek, AB T0X 3T5 Traditional Territory of the Treaty 8 People
• Colors that are in logo
• Banner or picture on back
• Ability to put different names and contacts
• Website: kolbymarsh.ca
• "Project Planning, Management, Inspection & Consulting for Canada's Petroleum Industry"

```html
<!DOCTYPE html>
<html lang="en">
<head>
<meta charset="utf-8">
<title>KolbyMarsh Inc. – Business Card</title>
<link rel="stylesheet" href="https://fonts.googleapis.com/css2?family=Open+Sans:wght@400;600&display=swap">
<style>
  :root {
    --page-bg: #e9e7e4;
    --card-black: #050505;
    --card-glow: #1f1f1f;
    --brand-green: #6cbd45;
    --brand-blue: #2e3284;
    --brand-sky: #5b87c7;
    --text-white: #f2f2f2;
  }
  * { margin: 0; padding: 0; box-sizing: border-box; }
  html, body {
    width: 1200px; height: 844px; overflow: hidden;
    background: var(--page-bg);
    font-family: "Open Sans", Arial, sans-serif;
  }
  .layout {
    position: relative; width: 1200px; height: 844px;
    display: flex; align-items: center; justify-content: center; gap: 40px;
  }
  .card {
    position: relative; width: 520px; height: 297px; overflow: hidden;
    background: var(--card-black);
    box-shadow: 0 10px 28px rgba(0,0,0,.25);
  }
  /* Contact side */
  .card-contact .band-top {
    position: absolute; left: 0; top: 0; width: 100%; height: 14px;
    background: var(--brand-green);
  }
  .card-contact .band-bottom {
    position: absolute; left: 0; bottom: 0; width: 100%; height: 14px;
    background: var(--brand-blue);
  }
  .card-contact .corner-art {
    position: absolute; left: 0; bottom: 14px; width: 210px; height: 150px;
    background: radial-gradient(ellipse at 0% 100%, var(--brand-sky) 0%, var(--brand-blue) 45%, rgba(5,5,5,0) 75%);
  }
  .contact {
    position: absolute; left: 200px; right: 20px; top: 58px;
    text-align: center; color: var(--text-white);
  }
  .contact .name {
    color: var(--brand-green); font-weight: 600; font-size: 19px; margin-bottom: 26px;
  }
  .contact .lines,
  .contact .address { font-size: 13.5px; line-height: 20px; font-weight: 400; }
  .contact .address { margin-top: 14px; }

  /* Brand side */
  .card-brand {
    background: radial-gradient(ellipse at 55% 42%, var(--card-glow) 0%, var(--card-black) 70%);
  }
  .card-brand .tab-blue {
    position: absolute; right: 64px; top: 0; width: 36px; height: 20px;
    background: var(--brand-blue);
  }
  .card-brand .tab-green {
    position: absolute; left: 0; bottom: 58px; width: 34px; height: 38px;
    background: var(--brand-green);
  }
  .brand {
    position: absolute; left: 0; right: 0; top: 118px;
    display: flex; align-items: center; justify-content: center; gap: 14px;
  }
  .brand .dot {
    width: 22px; height: 22px; border-radius: 50%; background: var(--brand-green);
  }
  .brand .wordmark {
    color: var(--brand-green); font-weight: 600; font-size: 34px; letter-spacing: .5px;
  }
</style>
</head>
<body>
  <main class="layout">
    <section class="card card-contact" aria-label="Contact side">
      <div class="band-top"></div>
      <div class="corner-art" role="img" aria-label="Decorative brand-colour flourish"></div>
      <div class="contact">
        <p class="name">Reid Forbin</p>
        <p class="lines">555 418 9067<br>reid@kolbymarsh.ca<br>www.kolbymarsh.ca</p>
        <p class="address">RR4, Site2, Comp7<br>Harlow Creek, AB T0X 3T5</p>
      </div>
      <div class="band-bottom"></div>
    </section>

    <section class="card card-brand" aria-label="Brand side">
      <div class="tab-blue"></div>
      <div class="brand">
        <span class="dot"></span>
        <span class="wordmark">KolbyMarsh Inc.</span>
      </div>
      <div class="tab-green"></div>
    </section>
  </main>
</body>
</html>
```